Cool Landing page with email address sign up (mockups provided)

I need a landing page for a service that will send a weekly email to people who are looking for jobs in startups. On the landing page there is a call to action (submit button) to register their email address. The service is called VentureCrew and it is a side project to try to assist startup companies with hiring people.

I just want one single form field "Email".

The feeling I want to give people is one of adventure. Imagine the person is living in Gdansk Poland, they are a technical/IT expert and have dreams of making it big in a Startup in London. This is his big chance, this is going to allow him to do it! He's signing up to a big promise! It should be cool, professional, exciting.

A major influence should be:
http://brassteapotcorner.com/

There should also be a call to tweet in a cool way like on (http://www.withinfoundry.org/).

Look at this - taking a leap of faith, like this:
http://kitebloomapp.com/wp-content/uploads/2011/09/19.jpg

This is super with the colours - striking!:
http://pelvora.org/

Fly your kit higher!:
http://tobiasvrenn.com/

If necessary use sex to sell:
http://kitebloomapp.com/wp-content/uploads/2011/09/24.jpg

Some original art would work:
http://kitebloomapp.com/wp-content/uploads/2011/09/fx_ss_group1_sm_filtered_0000s_0007_Layer-14.jpg

This is effective for a call to action, I'm looking to you to act!:
http://kitebloomapp.com/wp-content/uploads/2011/09/weblance.jpg
Take inspiration from:
http://www.withinfoundry.org/
http://venturecrew.org/
http://quarrymint.com/

***N.B.: I would prefer original art background over a photo

Also:
http://pixelfolioroom.com/inspiration/a-showcase-of-landing-pages-designed-for-conversion
especially:
http://pixelfolioroom.com/wp-content/uploads/2011/09/01-landing.jpg
http://pixelfolioroom.com/wp-content/uploads/2011/09/04-landing.jpg
http://pixelfolioroom.com/wp-content/uploads/2011/10/texture21.jpg

I really like the colouring from Tinker Ledger:
http://board.quillmatic.com/

Reason: I'm going to be away for a few days so I won't have enough time to properly provide feedback.

The payment is now guaranteed. This project is a single page only.

I've added a few more example landing pages that I like.

I've now added the venturecrew logo image that should be used.

I've updated brief with more examples of what I'm looking for

Reason: I'm still progressing with candidate designs.

Target Market(s)

Technical people, english not being their native language. Ambitious to work in London/Dublin in a tech startup company. They want to receive a weekly emails with startup jobs in london or dublin.

Requirements
Must have
• Eyes must be drawn to the email registration form to get them to submit their email address. The background image or website theme should encourage their desires to work in the big city in exciting startup companies.

Should have a prompt to tweet (once pressed I'll do my own popup)

```html
<!DOCTYPE html>
<html lang="en">
<head>
<meta charset="utf-8">
<title>VentureCrew — Weekly Startup Jobs</title>
<link rel="stylesheet" href="https://fonts.googleapis.com/css2?family=Libre+Bodoni:ital,wght@1,400&family=Montserrat:wght@700&family=Ubuntu:wght@400;700&display=swap">
<style>
  :root {
    --sky-top: #0f8fc4;
    --sky-mid: #0a4f94;
    --sky-deep: #07306a;
    --sky-night: #061f4a;
    --skyline: #07203f;
    --white: #ffffff;
    --panel-fill: rgba(120, 160, 200, 0.42);
    --panel-edge: rgba(20, 40, 80, 0.75);
    --field-bg: #ffffff;
    --field-text: #4a4a4a;
    --button-top: #f2f2f2;
    --button-bottom: #c4c4c4;
    --button-text: #8a8a8a;
  }
  * { margin: 0; padding: 0; box-sizing: border-box; }
  html, body { width: 1200px; height: 1200px; overflow: hidden; }
  body {
    position: relative;
    background:
      radial-gradient(ellipse 700px 380px at 540px 20px, rgba(40, 180, 230, 0.55), transparent 70%),
      radial-gradient(ellipse 500px 400px at 1150px 420px, rgba(30, 140, 210, 0.35), transparent 70%),
      linear-gradient(180deg, var(--sky-mid) 0%, var(--sky-deep) 55%, var(--sky-night) 100%);
    font-family: "Ubuntu", sans-serif;
    color: var(--white);
  }

  .quote {
    position: absolute;
    top: 86px;
    right: 140px;
    text-align: right;
  }
  .quote-text {
    font-family: "Libre Bodoni", serif;
    font-style: italic;
    font-size: 39px;
    line-height: 42px;
    letter-spacing: 0.5px;
  }
  .quote-author {
    margin-top: 16px;
    margin-right: 42px;
    font-family: "Montserrat", sans-serif;
    font-weight: 700;
    font-size: 18px;
  }

  .social {
    position: absolute;
    top: 320px;
    right: 183px;
    display: flex;
    align-items: center;
    gap: 10px;
  }
  .social-tweet {
    display: flex;
    align-items: center;
    gap: 6px;
    font-family: "Ubuntu", sans-serif;
    font-weight: 700;
    font-size: 16px;
    color: var(--white);
    margin-right: 4px;
  }
  .social-tweet-mark {
    width: 10px; height: 10px;
    border-radius: 50%;
    background: var(--white);
  }
  .social-icon { width: 40px; height: 40px; display: block; }

  .signup {
    position: absolute;
    left: 345px;
    top: 508px;
    width: 506px;
    height: 312px;
    border-radius: 24px;
    background: var(--panel-fill);
    border: 2px solid var(--panel-edge);
    box-shadow: inset 0 2px 0 rgba(255,255,255,0.25), 0 4px 10px rgba(0,0,0,0.35);
  }
  .signup-field {
    position: absolute;
    left: 59px;
    top: 63px;
    width: 388px;
    height: 61px;
    background: var(--field-bg);
    border: 2px solid rgba(200, 210, 220, 0.9);
    box-shadow: inset 0 3px 5px rgba(0,0,0,0.25);
    padding: 0 16px;
    font-family: "Ubuntu", sans-serif;
    font-size: 17px;
    letter-spacing: 0.6px;
    color: var(--field-text);
    display: flex;
    align-items: center;
  }
  .signup-button {
    position: absolute;
    left: 59px;
    top: 166px;
    width: 388px;
    height: 79px;
    border-radius: 6px;
    background: linear-gradient(180deg, var(--button-top), var(--button-bottom));
    border: 1px solid rgba(255,255,255,0.7);
    box-shadow: 0 3px 6px rgba(0,0,0,0.35);
    font-family: "Ubuntu", sans-serif;
    font-weight: 700;
    font-size: 35px;
    letter-spacing: 1.5px;
    color: var(--button-text);
    text-shadow: 0 1px 0 rgba(255,255,255,0.8), 0 -1px 0 rgba(0,0,0,0.25);
    display: flex;
    align-items: center;
    justify-content: center;
  }

  .skyline {
    position: absolute;
    left: 0;
    bottom: 0;
    width: 1200px;
    height: 160px;
    background: linear-gradient(180deg, #0b3465 0%, var(--skyline) 60%);
  }
</style>
</head>
<body>
  <blockquote class="quote">
    <p class="quote-text">“A journey of<br>a thousand miles<br>must begin with<br>a single step.”</p>
    <p class="quote-author">— Orin Vale</p>
  </blockquote>

  <nav class="social" aria-label="Share and follow">
    <span class="social-tweet"><span class="social-tweet-mark"></span>Chirpline</span>
    <svg class="social-icon" viewBox="0 0 40 40" aria-label="Email">
      <rect x="0" y="0" width="40" height="40" fill="#0a3a78"/>
      <rect x="7" y="11" width="26" height="18" fill="#ffffff"/>
      <polyline points="7,11 20,22 33,11" fill="none" stroke="#0a3a78" stroke-width="2.5"/>
    </svg>
    <svg class="social-icon" viewBox="0 0 40 40" aria-label="Feed">
      <rect x="0" y="0" width="40" height="40" fill="#0a3a78"/>
      <circle cx="11" cy="29" r="3.5" fill="#ffffff"/>
      <path d="M8 19 A13 13 0 0 1 21 32" fill="none" stroke="#ffffff" stroke-width="3.5"/>
      <path d="M8 10 A22 22 0 0 1 30 32" fill="none" stroke="#ffffff" stroke-width="3.5"/>
    </svg>
  </nav>

  <form class="signup" aria-label="Weekly startup jobs sign-up">
    <div class="signup-field">Your e-mail here</div>
    <div class="signup-button">SUBSCRIBE</div>
  </form>

  <div class="skyline" role="img" aria-label="Night city skyline with lit office windows"></div>
</body>
</html>
```